Medical Device Company needs website

We are a start-up medical device company looking to sell boot (foot) and brace (ankle) products on Shopify. We are still working on the name but you can use Tavrix as a placeholder- no logo yet)

Website information:
- Look: modern/tech with clean lines and symmetry.
- Colors: teal, white, black, and greys.
- Headers: home, shop, about us, help, blog
- Icons (upper right): search, my account and shopping cart
-place to sign up for newsletter

```html
<!DOCTYPE html>
<html lang="en">
<head>
<meta charset="utf-8">
<title>Tavrix — Medical Boots &amp; Braces</title>
<link rel="stylesheet" href="https://fonts.googleapis.com/css2?family=Josefin+Sans:wght@400;600;700&family=Poppins:wght@400;500;600&display=swap">
<style>
:root{
  --teal:#0f7c77;
  --teal-dark:#0a5f5b;
  --teal-light:#1f9a93;
  --ink:#1b1b1b;
  --grey:#5d6466;
  --grey-light:#eef1f1;
  --white:#ffffff;
}
*{box-sizing:border-box;margin:0;padding:0}
html,body{width:1200px;height:3836px;overflow:hidden;background:var(--white)}
body{font-family:"Poppins",sans-serif;color:var(--ink);position:relative}
a{color:inherit;text-decoration:none}

/* nav */
.site-nav{position:absolute;top:0;left:0;width:1200px;height:70px;display:flex;align-items:center;padding:0 110px;border-bottom:1px solid #e6e9e9}
.nav-links{display:flex;gap:26px;font-family:"Josefin Sans",sans-serif;font-size:13px;font-weight:600;letter-spacing:.5px}
.nav-links .active{color:var(--teal);border-bottom:2px solid var(--teal);padding-bottom:3px}
.brand{position:absolute;left:50%;transform:translateX(-50%);font-family:"Josefin Sans",sans-serif;font-weight:700;font-size:26px;letter-spacing:2px;color:var(--teal)}
.nav-icons{margin-left:auto;display:flex;gap:14px}
.nav-icons span{width:30px;height:30px;border:1.5px solid var(--ink);border-radius:50%;display:flex;align-items:center;justify-content:center}

/* hero */
.hero{position:absolute;top:70px;left:0;width:1200px;height:370px;overflow:hidden;background:#f4f6f6}
.hero-photo{position:absolute;left:420px;top:0;width:780px;height:370px;background:linear-gradient(120deg,#e9ecec 0%,#c9cfd0 35%,#8f9ea0 60%,#b59a7c 80%,#6f7b7d 100%)}
.hero-fade{position:absolute;left:420px;top:0;width:260px;height:370px;background:linear-gradient(90deg,#f4f6f6,rgba(244,246,246,0))}
.hero-copy{position:absolute;left:110px;top:80px;width:380px}
.hero-copy h1{font-family:"Josefin Sans",sans-serif;font-size:32px;font-weight:700;letter-spacing:1px;margin-bottom:14px}
.hero-copy h1 em{font-style:normal;color:var(--teal)}
.hero-copy p{font-size:13.5px;line-height:24px;color:var(--grey);margin-bottom:28px}
.btn{display:inline-block;background:var(--teal);color:var(--white);font-family:"Josefin Sans",sans-serif;font-weight:700;font-size:12px;letter-spacing:1px;padding:11px 22px;border-radius:4px}
.btn-light{background:var(--white);color:var(--teal)}

/* titles */
.section-title{position:absolute;left:0;width:1200px;text-align:center;font-family:"Josefin Sans",sans-serif;font-weight:700;font-size:28px;letter-spacing:1px}
.section-title em{font-style:normal;color:var(--teal);border-bottom:2px solid var(--teal)}
.center-btn{position:absolute;left:0;width:1200px;text-align:center}

/* categories */
.categories{position:absolute;top:590px;left:100px;width:1000px;display:grid;grid-template-columns:repeat(4,1fr)}
.category{text-align:center}
.category .thumb{width:180px;height:180px;border-radius:50%;margin:0 auto 22px}
.category h3{font-family:"Josefin Sans",sans-serif;font-size:14px;font-weight:600;letter-spacing:.5px}

/* about */
.about{position:absolute;top:960px;left:0;width:1200px;height:540px;background:linear-gradient(135deg,var(--teal-dark),var(--teal) 55%,var(--teal-light))}
.about-photo-a{position:absolute;left:110px;top:92px;width:300px;height:330px;border-radius:14px;background:linear-gradient(150deg,#eef2f3,#b9c3c6 60%,#5b6a6e)}
.about-photo-b{position:absolute;left:300px;top:150px;width:310px;height:380px;border-radius:14px;background:linear-gradient(160deg,#f2f4f4,#cfd5d6 40%,#2a2d2f 75%,#111)}
.about-copy{position:absolute;left:680px;top:70px;width:420px;color:var(--white)}
.about-copy h2{font-family:"Josefin Sans",sans-serif;font-size:26px;font-weight:700;letter-spacing:1px;display:inline-block;border-bottom:2px solid var(--white);margin-bottom:26px}
.about-copy p{font-size:13.5px;line-height:25px;margin-bottom:30px}

/* products */
.products{position:absolute;top:1620px;left:110px;width:980px;display:grid;grid-template-columns:repeat(4,1fr);gap:22px}
.product{height:356px;background:var(--white);border:1px solid #e3e7e7;border-radius:8px;box-shadow:0 4px 14px rgba(0,0,0,.08);position:relative;text-align:center;padding-top:30px}
.product .fav{position:absolute;top:12px;right:12px;width:26px;height:26px;border:1.5px solid var(--teal);border-radius:50%;display:flex;align-items:center;justify-content:center}
.product .thumb{width:160px;height:170px;margin:0 auto 28px;border-radius:6px}
.product h3{font-family:"Josefin Sans",sans-serif;color:var(--teal);font-size:16px;font-weight:700;letter-spacing:.5px}
.product .price{font-size:12px;color:var(--ink);margin:12px 0 20px}
.btn-small{display:inline-block;background:var(--teal);color:var(--white);font-family:"Josefin Sans",sans-serif;font-weight:700;font-size:10px;padding:8px 13px;border-radius:3px;letter-spacing:.5px}

/* promos */
.promos{position:absolute;top:2130px;left:110px;width:980px;display:grid;grid-template-columns:1fr 1fr;gap:16px}
.promo{height:320px;border-radius:12px;position:relative;overflow:hidden;color:var(--white)}
.promo-a{background:linear-gradient(150deg,#d7d1c8,#8a8580 50%,#2a2a2a)}
.promo-b{background:linear-gradient(150deg,#cfd2d3,#707679 45%,#1f2224)}
.promo::after{content:"";position:absolute;inset:0;background:linear-gradient(0deg,rgba(0,0,0,.65),rgba(0,0,0,0) 65%)}
.promo-copy{position:absolute;left:26px;bottom:28px;width:320px;z-index:1}
.promo-copy h3{font-family:"Josefin Sans",sans-serif;font-size:14px;font-weight:700;margin-bottom:8px}
.promo-copy p{font-size:11px;line-height:17px;margin-bottom:12px}
.btn-tiny{display:inline-block;background:var(--white);color:var(--teal);font-family:"Josefin Sans",sans-serif;font-weight:700;font-size:9px;padding:6px 10px;border-radius:3px}

/* news */
.news{position:absolute;top:2610px;left:110px;width:980px;display:grid;grid-template-columns:repeat(3,1fr);gap:16px}
.post{text-align:center}
.post .thumb{height:210px;border-radius:10px;margin-bottom:22px}
.post h3{font-family:"Josefin Sans",sans-serif;font-size:16px;font-weight:600;color:var(--teal);line-height:24px;letter-spacing:.5px}
.post time{display:block;font-size:12px;color:var(--grey);margin:16px 0 12px;letter-spacing:.5px}
.post p{font-size:12.5px;line-height:23px;color:var(--grey);padding:0 14px}

/* newsletter */
.newsletter{position:absolute;top:3180px;left:0;width:1200px;height:250px;background:linear-gradient(135deg,var(--teal-dark),var(--teal) 60%,var(--teal-light));text-align:center;color:var(--white)}
.newsletter h2{font-family:"Josefin Sans",sans-serif;font-size:26px;font-weight:600;letter-spacing:1px;margin-top:62px}
.newsletter p{font-family:"Josefin Sans",sans-serif;font-weight:600;font-size:14px;letter-spacing:.5px;margin-top:18px}
.signup{display:flex;justify-content:center;gap:10px;margin-top:34px}
.signup .field{width:300px;height:32px;border:1px solid rgba(255,255,255,.7);background:rgba(0,0,0,.25);border-radius:3px;font-size:10px;text-align:left;padding:10px 12px}
.signup .submit{height:32px;background:var(--white);color:var(--teal);font-family:"Josefin Sans",sans-serif;font-weight:700;font-size:10px;padding:11px 14px;border-radius:3px}

/* footer */
.site-footer{position:absolute;top:3430px;left:0;width:1200px;height:406px}
.footer-brand{position:absolute;left:110px;top:52px;font-family:"Josefin Sans",sans-serif;font-size:40px;font-weight:700;color:var(--teal);letter-spacing:2px}
.contact{position:absolute;left:110px;top:124px;width:260px;list-style:none;font-size:12px}
.contact li{display:flex;gap:12px;align-items:flex-start;margin-bottom:22px;line-height:20px}
.contact .ico{flex:none;width:22px;height:22px;border-radius:50%;background:var(--teal);display:flex;align-items:center;justify-content:center}
.footer-col{position:absolute;top:60px;font-size:12px}
.footer-col h4{font-family:"Josefin Sans",sans-serif;font-size:19px;font-weight:600;letter-spacing:1px;margin-bottom:18px}
.footer-col ul{list-style:none}
.footer-col li{margin-bottom:15px}
.footer-rule{position:absolute;left:110px;top:350px;width:980px;border-top:1px solid #cfd5d5}
.copyright{position:absolute;left:0;top:366px;width:1200px;text-align:center;font-size:11px;letter-spacing:.5px}
</style>
</head>
<body>

<header class="site-nav">
  <nav class="nav-links">
    <a class="active">HOME</a><a>SHOP</a><a>ABOUT US</a><a>HELP</a><a>BLOG</a>
  </nav>
  <div class="brand">TAVRIX</div>
  <div class="nav-icons">
    <span><svg width="14" height="14" viewBox="0 0 14 14" fill="none" stroke="#1b1b1b" stroke-width="1.6"><circle cx="6" cy="6" r="4.2"/><path d="M9.2 9.2L13 13"/></svg></span>
    <span><svg width="14" height="14" viewBox="0 0 14 14" fill="none" stroke="#1b1b1b" stroke-width="1.6"><circle cx="7" cy="4.5" r="2.8"/><path d="M1.8 13c.6-3 2.7-4.4 5.2-4.4s4.6 1.4 5.2 4.4"/></svg></span>
    <span><svg width="14" height="14" viewBox="0 0 14 14" fill="none" stroke="#1b1b1b" stroke-width="1.6"><path d="M1 1.5h2l1.6 7.5h7L13 4H4"/><circle cx="5.5" cy="12" r="1"/><circle cx="10.5" cy="12" r="1"/></svg></span>
  </div>
</header>

<section class="hero">
  <div class="hero-photo" role="img" aria-label="Pharmacist helping a seated customer in a wheelchair try on an ankle brace in a medical supply store"></div>
  <div class="hero-fade"></div>
  <div class="hero-copy">
    <h1>WELCOME TO <em>TAVRIX</em></h1>
    <p>Lorem ipsum dolor sit amet, consectetur adipiscing elit, sed do eiusmod tempor incididunt ut labore et dolore magna aliqua enim ad minim veniam.</p>
    <a class="btn">SHOP NOW</a>
  </div>
</section>

<h2 class="section-title" style="top:506px">SHOP BY <em>CATEGORY</em></h2>
<div class="categories">
  <div class="category"><div class="thumb" role="img" aria-label="Foot wearing a soft walking boot" style="background:linear-gradient(150deg,#e6eef7,#b9cbe0)"></div><h3>FOOT BOOTS</h3></div>
  <div class="category"><div class="thumb" role="img" aria-label="Ankle wrapped in a support brace" style="background:linear-gradient(150deg,#e9ddd3,#a88a77)"></div><h3>ANKLE BRACES</h3></div>
  <div class="category"><div class="thumb" role="img" aria-label="Rehabilitation accessories laid out on a table" style="background:linear-gradient(150deg,#e4e8ec,#9aa6b2)"></div><h3>REHABILITATION ACCESSORIES</h3></div>
  <div class="category"><div class="thumb" role="img" aria-label="Assorted recovery product boxes and bottles" style="background:linear-gradient(150deg,#eee6f0,#b48fa5 60%,#6b83b0)"></div><h3>RECOVERY PRODUCTS</h3></div>
</div>
<div class="center-btn" style="top:856px"><a class="btn">VIEW MORE</a></div>

<section class="about">
  <div class="about-photo-a" role="img" aria-label="Person in a wheelchair with a foot boot"></div>
  <div class="about-photo-b" role="img" aria-label="Black walking boot brace shown close up"></div>
  <div class="about-copy">
    <h2>ABOUT US</h2>
    <p>Lorem ipsum dolor sit amet, consectetur adipiscing elit, sed do eiusmod tempor incididunt ut labore et dolore magna aliqua enim ad minim veniam quis nostrud exercitation ullamco laboris nisi ut aliquip ex ea commodo consequat duis aute irure dolor in reprehenderit in voluptate velit esse cillum dolore eu fugiat nulla pariatur.</p>
    <a class="btn btn-light">LEARN MORE</a>
  </div>
</section>

<h2 class="section-title" style="top:1546px">TRENDING <em>PRODUCTS</em></h2>
<div class="products">
  <div class="product"><span class="fav"><svg width="12" height="11" viewBox="0 0 12 11" fill="none" stroke="#0f7c77" stroke-width="1.3"><path d="M6 10S1 7 1 3.6A2.6 2.6 0 0 1 6 2.4a2.6 2.6 0 0 1 5 1.2C11 7 6 10 6 10z"/></svg></span><div class="thumb" role="img" aria-label="Grey padded walking boot" style="background:linear-gradient(160deg,#f1f3f5,#a7adb6)"></div><h3>LOREM IPSUM DOLOR</h3><p class="price">FROM $ 76.89</p><a class="btn-small">VIEW DETAILS</a></div>
  <div class="product"><span class="fav"><svg width="12" height="11" viewBox="0 0 12 11" fill="none" stroke="#0f7c77" stroke-width="1.3"><path d="M6 10S1 7 1 3.6A2.6 2.6 0 0 1 6 2.4a2.6 2.6 0 0 1 5 1.2C11 7 6 10 6 10z"/></svg></span><div class="thumb" role="img" aria-label="Pair of beige recovery boots" style="background:linear-gradient(160deg,#f6f1ea,#cdbfa9)"></div><h3>LOREM IPSUM DOLOR</h3><p class="price">FROM $ 23.87</p><a class="btn-small">VIEW DETAILS</a></div>
  <div class="product"><span class="fav"><svg width="12" height="11" viewBox="0 0 12 11" fill="none" stroke="#0f7c77" stroke-width="1.3"><path d="M6 10S1 7 1 3.6A2.6 2.6 0 0 1 6 2.4a2.6 2.6 0 0 1 5 1.2C11 7 6 10 6 10z"/></svg></span><div class="thumb" role="img" aria-label="White rigid ankle brace" style="background:linear-gradient(160deg,#f5f6f7,#c2c7cb)"></div><h3>LOREM IPSUM DOLOR</h3><p class="price">FROM $ 23.89</p><a class="btn-small">VIEW DETAILS</a></div>
  <div class="product"><span class="fav"><svg width="12" height="11" viewBox="0 0 12 11" fill="none" stroke="#0f7c77" stroke-width="1.3"><path d="M6 10S1 7 1 3.6A2.6 2.6 0 0 1 6 2.4a2.6 2.6 0 0 1 5 1.2C11 7 6 10 6 10z"/></svg></span><div class="thumb" role="img" aria-label="Skin tone elastic support sleeve" style="background:linear-gradient(160deg,#f8e4d6,#d49a78)"></div><h3>LOREM IPSUM DOLOR</h3><p class="price">FROM $ 19.65</p><a class="btn-small">VIEW DETAILS</a></div>
</div>
<div class="center-btn" style="top:2016px"><a class="btn">VIEW MORE PRODUCTS</a></div>

<div class="promos">
  <div class="promo promo-a" role="img" aria-label="Physiotherapist examining a patient's ankle">
    <div class="promo-copy"><h3>LOREM IPSUM DOLOR</h3><p>Lorem ipsum dolor sit amet, consectetur adipiscing elit, sed do eiusmod tempor incididunt ut labore et dolore.</p><span class="btn-tiny">EXPLORE NOW</span></div>
  </div>
  <div class="promo promo-b" role="img" aria-label="Leg in a black walking boot on a clinic floor">
    <div class="promo-copy"><h3>LOREM IPSUM DOLOR</h3><p>Lorem ipsum dolor sit amet, consectetur adipiscing elit, sed do eiusmod tempor.</p><span class="btn-tiny">EXPLORE NOW</span></div>
  </div>
</div>

<h2 class="section-title" style="top:2528px">LATEST <em>NEWS &amp; BLOGS</em></h2>
<div class="news">
  <article class="post"><div class="thumb" role="img" aria-label="Pair of suede ankle boots on a wooden floor" style="background:linear-gradient(150deg,#d9e0e4,#8d8276 60%,#4d4540)"></div><h3>LOREM IPSUM DOLOR SIT<br>AMET ADIPISCING</h3><time>20TH APRIL 2024</time><p>Lorem ipsum dolor sit amet, consectetur adipiscing elit, sed do eiusmod tempor incididunt ut labore</p></article>
  <article class="post"><div class="thumb" role="img" aria-label="Foot in a walking boot beside a crutch" style="background:linear-gradient(150deg,#1e2b3a,#4d5563 55%,#c8c3bd)"></div><h3>LOREM IPSUM DOLOR SIT<br>AMET ADIPISCING</h3><time>09TH APRIL 2024</time><p>Lorem ipsum dolor sit amet, consectetur adipiscing elit, sed do eiusmod tempor incididunt ut labore</p></article>
  <article class="post"><div class="thumb" role="img" aria-label="Hands fitting an ankle brace on a patient" style="background:linear-gradient(150deg,#e9e2da,#b7a79a 55%,#5e6e7a)"></div><h3>LOREM IPSUM DOLOR SIT<br>AMET ADIPISCING</h3><time>10TH JUNE 2024</time><p>Lorem ipsum dolor sit amet, consectetur adipiscing elit, sed do eiusmod tempor incididunt ut labore</p></article>
</div>
<div class="center-btn" style="top:3076px"><a class="btn">VIEW MORE NEWS</a></div>

<section class="newsletter">
  <h2>SUBSCRIBE TO OUR NEWSLETTER</h2>
  <p>BE THE FIRST TO KNOW ABOUT NEW COLLECTIONS AND EXCLUSIVE OFFERS.</p>
  <div class="signup"><span class="field">EMAIL ADDRESS</span><span class="submit">SUBSCRIBE NOW</span></div>
</section>

<footer class="site-footer">
  <div class="footer-brand">TAVRIX</div>
  <ul class="contact">
    <li><span class="ico"><svg width="11" height="11" viewBox="0 0 12 12" fill="#fff"><path d="M3 1l2 2.5-1.2 1.3c.6 1.3 1.6 2.3 2.9 2.9L8 6.5 10.5 8.5 9.5 11C5 10.8 1.2 7 1 2.5z"/></svg></span>+1 555 010 2040</li>
    <li><span class="ico"><svg width="11" height="9" viewBox="0 0 12 9" fill="none" stroke="#fff" stroke-width="1.2"><rect x=".6" y=".6" width="10.8" height="7.8"/><path d="M.6.6L6 5l5.4-4.4"/></svg></span>INFO@TAVRIX.COM</li>
    <li><span class="ico"><svg width="9" height="12" viewBox="0 0 9 12" fill="#fff"><path d="M4.5 0A4.4 4.4 0 0 0 0 4.4C0 7.6 4.5 12 4.5 12S9 7.6 9 4.4A4.4 4.4 0 0 0 4.5 0zm0 6a1.6 1.6 0 1 1 0-3.2 1.6 1.6 0 0 1 0 3.2z"/></svg></span>56 TAVRIX LOREM LIPSUM AMET<br>806 783</li>
  </ul>
  <div class="footer-col" style="left:480px"><h4>QUICK LINKS</h4><ul><li>HOME</li><li>SHOP</li><li>ABOUT US</li><li>HELP</li><li>BLOG</li></ul></div>
  <div class="footer-col" style="left:676px"><h4>OTHER LINKS</h4><ul><li>PRIVACY POLICY</li><li>TERMS &amp; CONDITIONS</li><li>HELP CENTER</li><li>TERM OF USE</li></ul></div>
  <div class="footer-col" style="left:896px"><h4>PRODUCTS</h4><ul><li>FOOT BOOTS</li><li>ANKLE BRACES</li><li>RECOVERY PRODUCTS</li><li>REHABILITATION ACCESSORIES</li></ul></div>
  <div class="footer-rule"></div>
  <p class="copyright">© COPYRIGHT 2024 ALL RIGHTS RESERVED | TAVRIX</p>
</footer>

</body>
</html>
```